IT Management and Consulting company wants a design

The website should transfer an innovative, forward-oriented, optimistic, and serious image to my customer. Because we work in an agile, the design should transfer this approach.

The new color should make a serious, but not boring, impression for the business visitors of top-level companies.

The main focus topics are:
* IT strategy consulting
* Digital transformation
* IT quality management

The website should be in the English language.

The website should be created for WordPress. The existing website is http://www.quorva-advisory.com (no WordPress) is provided by servalink.de. A WordPress sandbox system exists.

Target Market(s)

Purchasing departments, IT decision makers from companies, project recruiting companies

Industry/Entity Type

IT-Provider, Telecommunication, Automotive

Number of Pages Required

4 page

Font styles to use
Serif
Sans Serif

Requirements
Must have
• Long-pager scrolling, a detail page for each portfolio topics, contact page, page about the company
Nice to have
• Parallax animation less is more, maybe a nice Hero Video Header, interessting 3D graph, Isometric graphs will bi nice, more clean than overloaded,
Should not have
• personal recruting page like in www.quorva-advisory.com

```html
<!DOCTYPE html>
<html lang="en">
<head>
<meta charset="utf-8">
<title>Quorva Advisory – IT Management &amp; Consulting</title>
<link href="https://fonts.googleapis.com/css2?family=Rajdhani:wght@400;500;600;700&family=Arimo:wght@400;700&display=swap" rel="stylesheet">
<style>
:root{
  --gold:#ad6a05;
  --gold-dark:#955b03;
  --grey:#8b8b8d;
  --grey-dark:#7a7a7c;
  --ink:#3b3b3b;
  --body:#555;
  --white:#fff;
  --line:#e6e6e6;
}
*{box-sizing:border-box;margin:0;padding:0}
html,body{width:1200px;height:3715px;overflow:hidden}
body{position:relative;background:var(--white);font-family:"Arimo",Arial,sans-serif;color:var(--ink)}
.abs{position:absolute}

/* header */
.top-rule{left:0;top:0;width:1200px;height:4px;background:var(--gold)}
.brand{display:flex;align-items:center;gap:10px}
.brand-mark{width:10px;height:10px;background:var(--ink)}
.brand-name{font-family:"Rajdhani",sans-serif;font-weight:600;color:var(--ink);font-size:28px;line-height:1}
.main-nav a{position:absolute;top:70px;font-family:"Rajdhani",sans-serif;font-weight:600;font-size:17px;color:var(--ink);text-decoration:none}
.main-nav a.active{color:var(--gold)}

/* hero */
.hero{left:0;top:146px;width:1200px;height:728px;background:radial-gradient(ellipse at 60% 45%,#4a3a2c 0%,#231d19 45%,#0f0e0e 100%)}
.hero-title{left:0;top:484px;width:1200px;text-align:center;font-family:"Rajdhani",sans-serif;font-weight:600;font-size:70px;color:var(--white)}
.hero-sub{left:0;top:560px;width:1200px;text-align:center;font-family:"Rajdhani",sans-serif;font-weight:500;font-size:30px;color:var(--white)}
.play{left:556px;top:618px;width:88px;height:88px}

/* about */
.about-frame{left:94px;top:935px;width:506px;height:496px;border:1px solid var(--gold)}
.about-photo{left:111px;top:953px;width:506px;height:497px;background:linear-gradient(135deg,#8c8f8c 0%,#c9c1ad 45%,#3d4658 100%)}
.section-h{font-family:"Rajdhani",sans-serif;font-weight:600;font-size:32px;color:var(--ink);letter-spacing:.5px}
.about-sub{left:666px;top:1044px;font-family:"Rajdhani",sans-serif;font-weight:600;font-size:21px;color:var(--gold)}
.about-text{left:666px;width:423px;font-size:13.5px;line-height:25.7px;color:var(--body);text-align:justify}
.btn-gold{display:flex;align-items:center;justify-content:center;background:var(--gold);color:var(--white);font-family:"Rajdhani",sans-serif;font-weight:600;font-size:17px}
.divider{height:1px;background:var(--line)}

/* services */
.center-h{left:0;width:1200px;text-align:center;font-family:"Rajdhani",sans-serif;font-weight:600;font-size:38px;color:var(--ink)}
.center-h span{color:var(--gold)}
.underline{height:3px;background:var(--gold)}
.card{top:1663px;width:312px;height:408px;background:var(--grey);color:var(--white);text-align:center}
.card.featured{background:var(--gold)}
.card-icon{position:absolute;left:96px;top:38px;width:120px;height:120px;border-radius:50%;background:var(--white);display:flex;align-items:center;justify-content:center}
.card-title{position:absolute;top:176px;width:100%;font-family:"Rajdhani",sans-serif;font-weight:700;font-size:24px}
.card-kicker{position:absolute;top:206px;width:100%;font-family:"Rajdhani",sans-serif;font-size:17px;letter-spacing:.5px}
.card-text{position:absolute;top:236px;left:30px;width:252px;font-size:13.5px;line-height:24px}
.card-btn{position:absolute;left:101px;top:329px;width:111px;height:40px;border:1px solid var(--white);display:flex;align-items:center;justify-content:center;font-family:"Rajdhani",sans-serif;font-weight:600;font-size:16px}

/* scouting */
.scout-band{left:0;top:2150px;width:1200px;height:561px;background:linear-gradient(90deg,#fdf8f4 0%,#fbf1e8 35%,#c6a27a 55%,#48617f 78%,#2c3e5a 100%)}
.scout-text{left:111px;top:2347px;width:372px;font-size:13.5px;line-height:25.7px;color:var(--body);text-align:justify}
.btn-grey{background:var(--grey);color:var(--white);display:flex;align-items:center;justify-content:center;font-family:"Rajdhani",sans-serif;font-weight:600;font-size:19px}

/* portfolio */
.tile{top:2853px;width:237px;height:262px}
.tile-photo{height:194px}
.tile-label{height:68px;display:flex;align-items:center;justify-content:center;color:var(--white);font-family:"Rajdhani",sans-serif;font-weight:700;font-size:16px;letter-spacing:.5px}

/* footer */
.footer{left:0;top:3205px;width:1200px;height:510px;background:var(--gold)}
.foot-nav a{position:absolute;top:3258px;font-family:"Rajdhani",sans-serif;font-weight:600;font-size:18px;color:var(--white);text-decoration:none}
.foot-rule{height:1px;background:rgba(255,255,255,.25)}
.foot-h{font-family:"Rajdhani",sans-serif;font-weight:700;font-size:19px;color:var(--white);letter-spacing:1px}
.field{background:var(--white);font-size:11px;color:#333;padding:10px 12px 0}
.submit{background:var(--grey);color:var(--white);font-size:13px;display:flex;align-items:center;justify-content:center}
.contact-icon{width:44px;height:44px;border:2px solid var(--white);border-radius:50%;display:flex;align-items:center;justify-content:center}
.contact-label{font-size:11px;color:var(--white);line-height:18px;font-family:"Rajdhani",sans-serif;font-weight:600}
.social{width:36px;height:36px;border:2px solid var(--white);border-radius:50%}
.copyright{left:0;top:3662px;width:1200px;text-align:center;font-family:"Rajdhani",sans-serif;font-size:16px;color:var(--white)}
</style>
</head>
<body>

<header>
  <div class="abs top-rule"></div>
  <div class="abs brand" style="left:111px;top:62px">
    <span class="brand-mark"></span><span class="brand-name">Quorva Advisory</span>
  </div>
  <nav class="main-nav">
    <a class="active" style="left:584px">Home</a>
    <a style="left:679px">About Us</a>
    <a style="left:797px">Portfolio</a>
    <a style="left:913px">Scouting</a>
    <a style="left:1031px">Contact</a>
  </nav>
</header>

<section>
  <div class="abs hero" role="img" aria-label="Hands holding a tablet with glowing financial charts and figures"></div>
  <h1 class="abs hero-title">Quorva Advisory</h1>
  <p class="abs hero-sub">Sed ut perspiciatis unde omnis iste natus error sit voluptatem</p>
  <svg class="abs play" viewBox="0 0 88 88" aria-label="Play video">
    <circle cx="44" cy="44" r="42" fill="#b06d08" stroke="rgba(255,255,255,.25)" stroke-width="4"/>
    <path d="M35 29 L61 44 L35 59 Z" fill="#fff"/>
  </svg>
</section>

<section>
  <div class="abs about-frame"></div>
  <div class="abs about-photo" role="img" aria-label="Two colleagues planning a project at a board with sticky notes"></div>
  <h2 class="abs section-h" style="left:666px;top:996px">ABOUT US</h2>
  <p class="abs about-sub">Mit Methode Professionell zum Projekterfolg</p>
  <p class="abs about-text" style="top:1088px">Whether IT project management, consulting, commissioning management or system integration: With Quorva Advisory you create the best conditions for IT systems that do what they should. In compliance with all time and cost specifications.Well-known companies from the automotive and telecommunications industries regularly use our individual management and consulting services.</p>
  <p class="abs about-text" style="top:1268px">Digital transformation: With our methodological competence in classic and agile projects, we can support you and help you to shape the transition from the old world of ideas to the new agile mindset.</p>
  <div class="abs btn-gold" style="left:669px;top:1370px;width:129px;height:45px">READ MORE</div>
  <div class="abs divider" style="left:111px;top:1532px;width:978px"></div>
</section>

<section>
  <h2 class="abs center-h" style="top:1572px">OUR <span>SERVICES</span></h2>
  <div class="abs underline" style="left:577px;top:1629px;width:46px"></div>

  <div class="abs card" style="left:111px">
    <div class="card-icon">
      <svg width="64" height="64" viewBox="0 0 64 64" fill="none" stroke="#8b8b8d" stroke-width="2.5">
        <rect x="6" y="10" width="40" height="30"/><path d="M14 40 L10 56 M38 40 L42 56 M26 40 V50"/>
        <rect x="12" y="16" width="8" height="6"/><rect x="12" y="27" width="8" height="6"/><path d="M24 19 H38 M24 30 H34"/>
        <circle cx="52" cy="14" r="4"/><path d="M52 18 V40 M52 24 L44 30 M52 40 L48 56 M52 40 L56 56"/>
      </svg>
    </div>
    <div class="card-title">IT STRATEGY</div>
    <div class="card-kicker">CONSULTING</div>
    <p class="card-text">A deliberately high standard for which we bundle all the qualities that important competence to meet them.</p>
    <div class="card-btn">READ MORE</div>
  </div>

  <div class="abs card featured" style="left:444px">
    <div class="card-icon">
      <svg width="64" height="64" viewBox="0 0 64 64" fill="none" stroke="#ad6a05" stroke-width="2.5">
        <rect x="22" y="22" width="20" height="20"/>
        <path d="M28 22 V10 M36 22 V10 M28 42 V54 M36 42 V54 M22 28 H10 M22 36 H10 M42 28 H54 M42 36 H54"/>
        <circle cx="28" cy="7" r="3"/><circle cx="36" cy="7" r="3"/><circle cx="28" cy="57" r="3"/><circle cx="36" cy="57" r="3"/>
        <circle cx="7" cy="28" r="3"/><circle cx="7" cy="36" r="3"/><circle cx="57" cy="28" r="3"/><circle cx="57" cy="36" r="3"/>
      </svg>
    </div>
    <div class="card-title">DIGITAL</div>
    <div class="card-kicker">TRANSFORMATION</div>
    <p class="card-text">A deliberately high standard for which we bundle all the qualities that important competence to meet them.</p>
    <div class="card-btn">READ MORE</div>
  </div>

  <div class="abs card" style="left:776px">
    <div class="card-icon">
      <svg width="64" height="64" viewBox="0 0 64 64" fill="none" stroke="#8b8b8d" stroke-width="2.5">
        <circle cx="14" cy="32" r="6"/><circle cx="46" cy="12" r="6"/><circle cx="50" cy="32" r="6"/><circle cx="46" cy="52" r="6"/>
        <path d="M20 32 H44 M19 29 L40 14 M19 35 L40 50"/>
      </svg>
    </div>
    <div class="card-title">IT QUALITY</div>
    <div class="card-kicker">MANAGEMENT</div>
    <p class="card-text">A deliberately high standard for which we bundle all the qualities that important competence to meet them.</p>
    <div class="card-btn">READ MORE</div>
  </div>
</section>

<section>
  <div class="abs scout-band" role="img" aria-label="Business team working with charts, tablet and laptop showing data overlays"></div>
  <h2 class="abs section-h" style="left:111px;top:2268px;font-size:38px">SCOUTING</h2>
  <div class="abs underline" style="left:111px;top:2321px;width:52px"></div>
  <p class="abs scout-text">Are you looking for a company with an unusually large scope for development - whether permanent or free? Quorva Advisory offers a lot of space for people with ideas and drive. If you also like the idea of helping to shape an expanding company in close contact with the management, we look forward to hearing from you!</p>
  <div class="abs btn-grey" style="left:111px;top:2528px;width:136px;height:49px">Read More</div>
</section>

<section>
  <h2 class="abs center-h" style="top:2760px">OUR <span>PORTFOLIO</span></h2>
  <div class="abs tile" style="left:111px">
    <div class="tile-photo" role="img" aria-label="Business people reviewing a tablet in a bright office" style="background:linear-gradient(135deg,#e9ecef,#7c838c 60%,#3b3f46)"></div>
    <div class="tile-label" style="background:var(--gold)">PROJECTS IN EXCELLENCE</div>
  </div>
  <div class="abs tile" style="left:358px">
    <div class="tile-photo" role="img" aria-label="Consultants analysing printed charts on a desk" style="background:linear-gradient(135deg,#f1f3f6,#b9c3cf 55%,#5b6876)"></div>
    <div class="tile-label" style="background:var(--grey)">CONSULTING IN EXCELLENCE</div>
  </div>
  <div class="abs tile" style="left:604px">
    <div class="tile-photo" role="img" aria-label="Hands on a laptop with glowing digital interface elements" style="background:linear-gradient(135deg,#1b2550,#5a3f9e 50%,#c06ad8 70%,#1a1f3a)"></div>
    <div class="tile-label" style="background:var(--gold)">DIGITALIZATION</div>
  </div>
  <div class="abs tile" style="left:851px">
    <div class="tile-photo" role="img" aria-label="Finger touching a glowing cloud symbol on a dark network background" style="background:radial-gradient(circle at 50% 35%,#3fa0c8,#17334d 45%,#0a1420)"></div>
    <div class="tile-label" style="background:var(--grey)">CLOUD TRANSITION</div>
  </div>
</section>

<footer>
  <div class="abs footer"></div>
  <nav class="foot-nav">
    <a style="left:338px">Home</a>
    <a style="left:437px">About Us</a>
    <a style="left:560px">Portfolio</a>
    <a style="left:680px">Scouting</a>
    <a style="left:802px">Contact</a>
  </nav>
  <div class="abs foot-rule" style="left:111px;top:3332px;width:978px"></div>

  <h3 class="abs foot-h" style="left:111px;top:3369px">CONTACT US</h3>
  <div class="abs field" style="left:111px;top:3421px;width:180px;height:35px">First Name :</div>
  <div class="abs field" style="left:301px;top:3421px;width:181px;height:35px">Last Name :</div>
  <div class="abs field" style="left:111px;top:3466px;width:180px;height:34px">Email :</div>
  <div class="abs field" style="left:301px;top:3466px;width:181px;height:34px">Phone :</div>
  <div class="abs field" style="left:111px;top:3509px;width:371px;height:52px">Message :</div>
  <div class="abs submit" style="left:108px;top:3572px;width:98px;height:34px">SUBMIT</div>

  <h3 class="abs foot-h" style="left:573px;top:3369px">ADDRESS</h3>
  <div class="abs contact-icon" style="left:564px;top:3416px">
    <svg width="18" height="18" viewBox="0 0 18 18" fill="none" stroke="#fff" stroke-width="2"><path d="M9 17 C4 11 3 9 3 7 A6 6 0 0 1 15 7 C15 9 14 11 9 17 Z"/><circle cx="9" cy="7" r="2"/></svg>
  </div>
  <div class="abs contact-label" style="left:620px;top:3422px">ADDRESS<br># 125 Lorem Ipsum Dummy</div>
  <div class="abs contact-icon" style="left:564px;top:3478px">
    <svg width="18" height="18" viewBox="0 0 18 18" fill="none" stroke="#fff" stroke-width="2"><path d="M4 2 L7 2 L8 6 L6 7.5 C7 10 8 11 10.5 12 L12 10 L16 11 L16 14 C16 15 15 16 14 16 C8 16 2 10 2 4 C2 3 3 2 4 2 Z"/></svg>
  </div>
  <div class="abs contact-label" style="left:623px;top:3485px">PHONE<br>000.121.1231</div>
  <div class="abs contact-icon" style="left:564px;top:3546px">
    <svg width="18" height="18" viewBox="0 0 18 18" fill="none" stroke="#fff" stroke-width="2"><rect x="2" y="4" width="14" height="10"/><path d="M2 4 L9 10 L16 4"/></svg>
  </div>
  <div class="abs contact-label" style="left:623px;top:3550px">EMAIL US<br>info@compnayname.com</div>

  <div class="abs brand" style="left:822px;top:3440px">
    <span class="brand-mark" style="background:#fff"></span><span class="brand-name" style="color:#fff">Quorva Advisory</span>
  </div>
  <div class="abs social" style="left:866px;top:3507px" aria-label="Social profile"></div>
  <div class="abs social" style="left:908px;top:3507px" aria-label="Social profile"></div>
  <div class="abs social" style="left:951px;top:3507px" aria-label="Social profile"></div>
  <div class="abs social" style="left:994px;top:3507px" aria-label="Social profile"></div>
  <div class="abs social" style="left:1038px;top:3507px" aria-label="Social profile"></div>

  <div class="abs foot-rule" style="left:111px;top:3634px;width:978px"></div>
  <p class="abs copyright">© Copyright 2021 Q Adv.All Rights Reserved</p>
</footer>

</body>
</html>
```